Basketball Coaching Presentation

Design and enhance a word document into a power point or google slides document. Document will be used in a interview setting to walk through my philosophy and concepts as the coach. i would like it to pop and have some basketballs, backboard, rim net, court type graphics added. My text my change, be edited or evolve over time. must be easy to edit in the future.
Make Cover page...i will insert my name later

```html
<!DOCTYPE html>
<html lang="en">
<head>
<meta charset="utf-8">
<title>Basketball Coaching Presentation</title>
<link href="https://fonts.googleapis.com/css2?family=Rubik:wght@800;900&family=Open+Sans:wght@400;600;700&display=swap" rel="stylesheet">
<style>
:root{
  --red:#b0301a;
  --orange:#ee7a2f;
  --peach:#f6b98c;
  --blush:#fce4d6;
  --grey:#e4e4e4;
  --ink:#2a2522;
  --dark:#1c1917;
  --muted:#b9b1ab;
  --paper:#ffffff;
}
*{margin:0;padding:0;box-sizing:border-box}
html,body{width:1200px;height:2194px;overflow:hidden;background:var(--paper)}
body{position:relative;font-family:"Open Sans",Arial,sans-serif;color:var(--ink)}
.slide{position:absolute;width:496px;height:278px;background:var(--paper);overflow:hidden;
  box-shadow:0 10px 28px rgba(0,0,0,.22)}
.col-l{left:61px}.col-r{left:636px}
.row1{top:263px}.row2{top:608px}.row3{top:952px}.row4{top:1297px}.row5{top:1641px}
.abs{position:absolute}
.ball{position:absolute;border-radius:50%;background:var(--peach)}
.ball.soft{background:var(--blush)}
.ball.grey{background:var(--grey)}
.ball.bold{background:var(--orange)}
.photo{position:absolute;overflow:hidden}
.photo.round{border-radius:50%}
.ring{border:5px solid var(--orange)}
.ring-red{border:4px solid var(--red)}
.warm{background:radial-gradient(circle at 40% 40%,#e9d6cb,#a58c80 70%,#5b4a42)}
.court{background:linear-gradient(160deg,#6a5a45,#2b2620 60%,#1b1a18)}
.arena{background:linear-gradient(135deg,#3c3326,#6e5a37 55%,#2a251d)}
.board{background:radial-gradient(circle at 55% 55%,#f4f4f2,#c9c4bf 55%,#4a3a33)}
.mono{background:linear-gradient(135deg,#9a9a9a,#4a4a4a 60%,#222)}
.leather{background:radial-gradient(circle at 30% 40%,#c8401f,#9a2a14 70%,#7e1f0e)}
.title{font-family:"Rubik",Arial,sans-serif;font-weight:800;color:var(--red);line-height:1.05}
.list{list-style:none}
.list li{position:relative;padding-left:14px}
.list li::before{content:"";position:absolute;left:2px;top:.45em;width:6px;height:6px;border-radius:50%;background:var(--orange)}
.on-dark{color:#fff}
.label{font-weight:700;color:var(--orange);font-size:8.5px;text-align:center}
.fine{font-size:5.6px;line-height:1.55;color:var(--muted);text-align:center}
</style>
</head>
<body>

<!-- Cover -->
<section class="slide col-l row1 cover">
  <div class="photo round ring mono" style="left:-24px;top:33px;width:264px;height:264px" role="img" aria-label="Black and white photo of a young player lifting a trophy with teammates cheering"></div>
  <div class="ball" style="left:286px;top:17px;width:34px;height:34px"></div>
  <div class="ball" style="left:413px;top:-2px;width:84px;height:84px"></div>
  <div class="ball" style="left:160px;top:46px;width:48px;height:48px"></div>
  <div class="ball" style="left:427px;top:218px;width:50px;height:50px"></div>
  <h1 class="title abs" style="left:271px;top:84px;font-size:25px;width:200px">Develop a winning basketball program</h1>
  <p class="abs" style="left:276px;top:216px;font-family:Rubik,sans-serif;font-weight:800;font-size:6.5px;color:var(--red);line-height:2.4">Sam Taylor Brooks – Coach<br>July 10 2023</p>
</section>

<!-- Mission -->
<section class="slide col-r row1 mission">
  <div class="abs leather" style="left:332px;top:0;width:164px;height:278px" role="img" aria-label="Close-up texture of a basketball surface"></div>
  <div class="photo" style="left:253px;top:62px;width:204px;height:167px;clip-path:polygon(20% 0,100% 0,80% 100%,0 100%);background:linear-gradient(120deg,#6b8fb0,#c9886a 55%,#e0673a)" role="img" aria-label="Coach handing a basketball to a young player"></div>
  <div class="abs" style="left:306px;top:198px;width:110px;height:39px;background:var(--orange);clip-path:polygon(8% 0,100% 0,92% 100%,0 100%);color:#fff;padding:9px 0 0 22px">
    <div style="font-size:7.5px;font-weight:700">Sam Taylor Brooks</div>
    <div style="font-size:4.5px;font-style:italic">CEO &amp; COACH</div>
  </div>
  <div class="ball bold" style="left:-6px;top:223px;width:76px;height:76px"></div>
  <h2 class="title abs" style="left:49px;top:58px;font-size:20px">Mission<br>Statement</h2>
  <ul class="list abs" style="left:48px;top:114px;width:180px;font-size:8px;line-height:16.8px;color:#5b4b7a">
    <li>Develop a winning basketball program on and off the court with an unwavering commitment to developing players/coaches with high character, unparalleled work ethic, unassailable integrity, leadership, and life skills.</li>
  </ul>
</section>

<!-- Team building -->
<section class="slide col-l row2 team">
  <div class="ball soft" style="left:-12px;top:-26px;width:76px;height:76px"></div>
  <div class="photo round ring warm" style="left:276px;top:-8px;width:224px;height:224px" role="img" aria-label="Team stacking hands together in the center"></div>
  <div class="ball bold" style="left:427px;top:218px;width:50px;height:50px;opacity:.85"></div>
  <h2 class="title abs" style="left:45px;top:35px;font-size:18px">Team Building<br>and Culture</h2>
  <ul class="list abs" style="left:45px;top:92px;width:240px;font-size:7.6px;line-height:10.6px">
    <li style="margin-bottom:3px">Coachable, Good attitude, Body Language, life/Practice Habits.</li>
    <li style="margin-bottom:3px">Respect; Coaches, Teaches, Family, Yourself, Friends, School, and Community</li>
    <li style="margin-bottom:3px">Look for a mentor and be a mentor.</li>
    <li style="margin-bottom:3px">Teach them to be part of something greater than themselves.</li>
    <li style="margin-bottom:3px">Retain high character kids, highly motivated, hard workers, unselfish, communicators.</li>
    <li style="margin-bottom:3px">Building confidence from practice, repetition, routines, and game experience.</li>
    <li>Teach Failure is one step closer to success.</li>
  </ul>
</section>

<!-- Practice -->
<section class="slide col-r row2 practice">
  <div class="photo court" style="left:0;top:0;width:240px;height:278px;clip-path:polygon(0 0,100% 0,78% 45%,100% 100%,0 100%)" role="img" aria-label="Players jumping for a rebound in a gym"></div>
  <svg class="abs" style="left:0;top:0" width="240" height="278" aria-hidden="true">
    <path d="M0 170 L70 278" stroke="#fff" stroke-width="5"/>
    <path d="M160 145 L85 278" stroke="#fff" stroke-width="5"/>
  </svg>
  <div class="ball" style="left:406px;top:10px;width:34px;height:34px"></div>
  <div class="ball soft" style="left:412px;top:198px;width:100px;height:100px"></div>
  <h2 class="title abs" style="left:245px;top:31px;font-size:18px">Practice<br>philosophy</h2>
  <ul class="list abs" style="left:245px;top:95px;width:235px;font-size:8.6px;line-height:10.6px">
    <li style="margin-bottom:4px">Practice is harder than games.</li>
    <li style="margin-bottom:4px">Every minute counts, detailed plans, work on weakness, enhance strengths.</li>
    <li style="margin-bottom:4px">Fundamental development, High IQ development.</li>
    <li style="margin-bottom:4px">Teach how to play (not just teach plays), Teach Actions</li>
    <li style="margin-bottom:4px">Create good habits for life and basketball.</li>
    <li>Create an environment to learn to play successfully in game stress (make good decisions).</li>
  </ul>
</section>

<!-- Teach actions -->
<section class="slide col-l row3 actions">
  <div class="abs leather" style="left:0;top:48px;width:290px;height:183px" role="img" aria-label="Close-up texture of a basketball surface"></div>
  <div class="photo round ring board" style="left:110px;top:50px;width:180px;height:180px" role="img" aria-label="Coach's whiteboard with a drawn basketball court and a marker"></div>
  <div class="ball" style="left:249px;top:11px;width:34px;height:34px"></div>
  <div class="ball soft" style="left:412px;top:198px;width:100px;height:100px"></div>
  <h2 class="title abs" style="left:306px;top:64px;font-size:18px">Teach Actions</h2>
  <p class="abs" style="left:312px;top:98px;width:160px;font-size:8px;line-height:16.8px">DHO, Drag, BD, Ghost, Pin down, Stagger Screen, Curls, Pops, Fades, Flash, Euro Cuts, Stacks, Slips, Shallow cuts, Shuffle cuts, Elevator Screens, GAG, V-cut, RPP, Shape up, Back Screens, Dives.</p>
</section>

<!-- Offensive -->
<section class="slide col-r row3 offense">
  <div class="abs" style="left:0;top:30px;width:270px;height:218px;background:var(--dark);clip-path:polygon(0 0,100% 0,72% 100%,0 100%)"></div>
  <div class="photo arena" style="left:207px;top:82px;width:289px;height:166px;clip-path:polygon(20% 0,100% 0,100% 100%,0 100%)" role="img" aria-label="Player leaping for a dunk in an arena"></div>
  <div class="ball" style="left:413px;top:-4px;width:84px;height:84px"></div>
  <h2 class="title abs" style="left:298px;top:33px;font-size:18px">Offensive<br>philosophy</h2>
  <ul class="list abs on-dark" style="left:33px;top:36px;width:195px;font-size:8.6px;line-height:10.6px">
    <li style="margin-bottom:4px">Transition, Fast Break, Organized freedom.</li>
    <li style="margin-bottom:4px">Dribble Drive, Attack, Drive, and kick, Create double gaps.</li>
    <li style="margin-bottom:4px">Motion offense, constant action, put the defense on its heels.</li>
    <li style="margin-bottom:4px">Run Actions, DHO, BD, Drag, Ghost Screens, Staggers, Elevator, Shuffle, Slip.</li>
    <li style="margin-bottom:4px">Quick sets, mismatches, read and react, and counters.</li>
    <li style="margin-bottom:4px">Great Spacing, timing and ball movement.</li>
    <li>Create open shots and get to the foul line.</li>
  </ul>
</section>

<!-- Defensive -->
<section class="slide col-l row4 defense">
  <div class="abs" style="left:227px;top:30px;width:269px;height:218px;background:var(--dark);clip-path:polygon(0 0,100% 0,100% 100%,29% 100%)"></div>
  <div class="photo arena" style="left:0;top:82px;width:289px;height:166px;clip-path:polygon(0 0,80% 0,100% 100%,0 100%)" role="img" aria-label="Two players in a one-on-one defensive stance on court"></div>
  <h2 class="title abs" style="left:40px;top:33px;width:140px;font-size:18px;text-align:center">Defensive<br>philosophy</h2>
  <ul class="list abs on-dark" style="left:304px;top:48px;width:160px;font-size:8px;line-height:10px">
    <li style="margin-bottom:4px">Speed up your opponent, make them uncomfortable, change looks.</li>
    <li style="margin-bottom:4px">Great team defense, weak side help, stunt, up the line, ball you man.</li>
    <li style="margin-bottom:4px">Close out, box out.</li>
    <li style="margin-bottom:4px">Trap corners, baseline shift, offensive charges, stay connected, help is coming.</li>
    <li style="margin-bottom:4px">Communication on every movement.</li>
    <li>Full court pressure and take their best players out of the game.</li>
  </ul>
</section>

<!-- System -->
<section class="slide col-r row4 system">
  <div class="ball soft" style="left:-7px;top:102px;width:186px;height:186px;opacity:.7"></div>
  <div class="ball grey" style="left:415px;top:-9px;width:94px;height:94px"></div>
  <div class="photo round ring-red warm" style="left:250px;top:69px;width:102px;height:102px" role="img" aria-label="Hand drawing a play on a clipboard"></div>
  <div class="photo round ring warm" style="left:368px;top:76px;width:80px;height:80px" role="img" aria-label="Team fist bump"></div>
  <div class="photo round ring board" style="left:305px;top:165px;width:144px;height:144px" role="img" aria-label="Whiteboard with a drawn basketball court"></div>
  <h2 class="title abs" style="left:62px;top:57px;font-size:18px">System</h2>
  <ul class="list abs" style="left:62px;top:92px;font-size:9px;line-height:18.6px">
    <li>Play Chess not Checkers.</li>
    <li>Multi man offense</li>
    <li>Multiple Defenses</li>
    <li>Press and speed up.</li>
    <li>Out Execute your opponent</li>
    <li>Out work your opponent</li>
  </ul>
</section>

<!-- Numbers -->
<section class="slide col-l row5 numbers">
  <div class="ball grey" style="left:412px;top:-14px;width:94px;height:94px"></div>
  <h2 class="title abs" style="left:0;top:24px;width:504px;font-size:18px;text-align:center">The game in numbers</h2>
  <div class="photo round ring-red warm" style="left:83px;top:75px;width:74px;height:74px" role="img" aria-label="Hand drawing a play on a clipboard"></div>
  <div class="photo round arena" style="left:211px;top:75px;width:74px;height:74px;border:3px solid #3a332d" role="img" aria-label="Two players competing one-on-one"></div>
  <div class="photo round ring-red board" style="left:340px;top:75px;width:74px;height:74px" role="img" aria-label="Whiteboard with a drawn basketball court"></div>
  <div class="abs" style="left:70px;top:164px;width:100px"><div class="label">By The Numbers</div><p class="fine" style="margin-top:6px">Make +2, Miss -2, Fouls -1, Assts +2, Fouls -1, Assists +2, T/O -2, Steals +2, Reb +1, Blk +1, O/C +5, Defl +1.</p></div>
  <div class="abs" style="left:198px;top:164px;width:100px"><div class="label">Game Goals</div><p class="fine" style="margin-top:6px">Steals (20), Assists (20), T/O (&lt;10), O/C (3), OP/S (&lt;40), T/S (&gt;60), Rbs (&gt;30), FG% (&gt;40), FT% (&gt;70)</p></div>
  <div class="abs" style="left:326px;top:164px;width:106px"><div class="label">Game Etiquette</div><p class="fine" style="margin-top:6px">Huddle FT, Warmups, Subs, Stretch, Body Language, Clean up, Pickup TM, Dress Code, Sportsmanship, time-outs.</p></div>
</section>

<!-- Life skills -->
<section class="slide col-r row5 life">
  <div class="ball soft" style="left:-16px;top:220px;width:70px;height:70px"></div>
  <div class="photo warm" style="left:267px;top:63px;width:82px;height:80px" role="img" aria-label="Team fist bump"></div>
  <div class="photo arena" style="left:354px;top:37px;width:106px;height:106px" role="img" aria-label="Player dunking in an arena"></div>
  <div class="photo arena" style="left:267px;top:149px;width:82px;height:81px" role="img" aria-label="Two players competing one-on-one"></div>
  <div class="photo warm" style="left:354px;top:149px;width:82px;height:81px" role="img" aria-label="Hand drawing a play on a clipboard"></div>
  <div class="ball bold" style="left:337px;top:133px;width:28px;height:28px"></div>
  <h2 class="title abs" style="left:60px;top:76px;font-size:18px">Life Skills</h2>
  <p class="abs" style="left:60px;top:104px;width:175px;font-size:8px;line-height:16.8px">Disciple, Prepare, mentally tough, Confidence, Resilient, Communication, Teamwork, Goals, Understand the numbers, Be creative, More than one way to win, Adapt, Trust, Be on time, little things matter, you are always being watched.</p>
</section>

</body>
</html>
```